SCEN Banner Ad Design

We need a banner ad design for the Scholarly Capital Exchange Network (SCEN). SCEN is an internet-based consortium whose goal is to empower the global population to invest efficiently in financial markets by learning to apply a variety of quantitative stock market prediction techniques developed by professors at top U.S. universities. These techniques have good predictive performance for different classes of financial assets comparable to large existing mutual funds in the US. With the advent of online trading platforms, an increasing number of individual investors participate in the stock market. However, most individuals lack awareness about the existence of these academic prediction methods. Also, personalized decision-making based on these methods cannot be achieved without the application of optimal quantitative tools.
SCEN makes these prediction methods, and the tools for the optimal allocation of resources between different assets, freely available to the general public through a web platform that allows the user to a) learn about the extensive research at top U.S. universities that shows financial markets have a predictable component and identify models and asset classes that suit their investment preferences and objectives; b) back test these diverse trading models, using decades of historical stock market data, that provide returns in line with top investment houses and funds; c) obtain future predictions based on the underlying models; d) update the amounts invested in each of several assets at regular intervals of time according to the predictions of these models; e) track the performance of his portfolio in real time; f) build his financial social network whereby he can gain insights from other users as well as mirror their trading strategies in real time; and g) access leading financial experts from both academia and industry, who are available to provide advice and answer questions. All of the above features are novel additions to internet-based resources available to the average user.
The banner ad will be used on several websites, but first likely on CareerLoop (a social network for job searches) and CodeHarbor (an online community for software developers/engineers). The ad should capture the theme (and SCEN’s mission) of empowering the individual investor (along with the academic emphasis of the site) and leave a little room to be able to custom tailor it to a specific user demographic. For example, on CodeHarbor the goal is to target tech savvy individuals who undertake financial investments on their own, so we will need room on the ad itself to insert a “catch phrase” that speaks to these users specifically. Similarly, on CareerLoop, we may opt to target financial asset managers and so will insert a phrase into the ad that reaches out to these types of users. You can insert a few different phrases that you come up with on different versions of the ad intended for different groups of users. Here are also a few sample "catch phrases" for you to work with:
SCEN - Control Your Investments Without The Fees
SCEN – Beat the Market. Without The Fees.
SCEN – Hack the Markets. Without the Fees.
The SCEN Beta– Hack the Ivory Tower.
SCEN – Democratizing The Investment Landscape
Finally, we are open to different color schemes, but for reference the current version of the SCEN site uses a bluish theme.
Investment

```html
<!DOCTYPE html>
<html lang="en">
<head>
<meta charset="utf-8">
<title>SCEN Banner – Beat the Market. Without The Fee</title>
<link rel="stylesheet" href="https://fonts.googleapis.com/css2?family=Marcellus+SC&display=swap">
<style>
  :root {
    --steel-light: #c4d0da;
    --steel-mid: #8fa2b2;
    --steel-deep: #6a7f91;
    --headline-white: #ffffff;
    --button-dark: #4a5057;
    --button-edge: #7b838b;
    --panel-white: #ffffff;
    --panel-shade: #e6ebef;
    --name-slate: #3f5f80;
    --tagline-gray: #5a5f66;
  }
  * { margin: 0; padding: 0; box-sizing: border-box; }
  html, body {
    width: 1200px;
    height: 148px;
    overflow: hidden;
    background: #ffffff;
  }
  .banner {
    position: relative;
    width: 1200px;
    height: 148px;
    overflow: hidden;
    font-family: "Marcellus SC", serif;
  }
  .banner__backdrop {
    position: absolute;
    inset: 0;
    background:
      radial-gradient(ellipse 70% 140% at 40% 10%, var(--steel-light) 0%, var(--steel-mid) 55%, var(--steel-deep) 100%);
  }
  .banner__headline {
    position: absolute;
    left: 74px;
    top: 28px;
    font-size: 41px;
    font-weight: 400;
    letter-spacing: 1px;
    color: var(--headline-white);
    text-shadow: 0 2px 3px rgba(40, 55, 70, 0.55);
    white-space: nowrap;
  }
  .banner__cta {
    position: absolute;
    left: 146px;
    top: 110px;
    width: 484px;
    height: 52px;
    border-radius: 14px;
    border: 2px solid var(--button-edge);
    background: linear-gradient(to bottom, #5e656c 0%, var(--button-dark) 60%);
    color: var(--headline-white);
    font-family: "Marcellus SC", serif;
    font-size: 34px;
    letter-spacing: 2px;
    text-align: center;
    line-height: 40px;
    text-decoration: none;
    box-shadow: 0 -2px 6px rgba(0, 0, 0, 0.25);
  }
  .banner__panel {
    position: absolute;
    top: 0;
    left: 740px;
    width: 460px;
    height: 148px;
  }
  .brand-name {
    position: absolute;
    left: 790px;
    width: 410px;
    top: 28px;
    text-align: center;
    font-family: "Marcellus SC", serif;
    font-weight: 400;
    font-size: 64px;
    line-height: 1;
    letter-spacing: 4px;
    color: var(--name-slate);
  }
  .tagline {
    position: absolute;
    left: 790px;
    width: 410px;
    top: 106px;
    text-align: center;
    font-family: "Marcellus SC", serif;
    font-size: 17px;
    letter-spacing: 2.4px;
    color: var(--tagline-gray);
    white-space: nowrap;
  }
</style>
</head>
<body>
  <div class="banner">
    <div class="banner__backdrop" role="img" aria-label="Blue-gray sunburst of radiating light rays behind the headline"></div>

    <h1 class="banner__headline">Beat the Market. Without The Fee</h1>
    <a class="banner__cta" href="#">Click Here</a>

    <svg class="banner__panel" viewBox="0 0 460 148" aria-hidden="true">
      <defs>
        <linearGradient id="panelFill" x1="0" y1="0" x2="1" y2="0">
          <stop offset="0" stop-color="#e6ebef"/>
          <stop offset="0.25" stop-color="#ffffff"/>
        </linearGradient>
      </defs>
      <path d="M52 0 Q28 74 40 148 L460 148 L460 0 Z" fill="url(#panelFill)"/>
    </svg>

    <p class="brand-name">SCEN</p>
    <p class="tagline">Empowering the Investor</p>
  </div>
</body>
</html>
```